LUMIVO Business Card

provide hypnotherapy and counselling for addictions, weight loss, anxiety, depression, smoking, alcohol etc
i would like the design to fit in with a feeling of peace and tranquility

Industry/Entity Type

Hypnotherapy

Contact Information for Business Card

Janet Callory
Clinical Hypnotherapist and Counsellor
BA Social Work
Dip Clinical Hypnotherapy and Psychotherapy

Phone: 0438157302
Email: astillbrookhypnotherapy@fernmail.example

```html
<!DOCTYPE html>
<html lang="en">
<head>
<meta charset="utf-8">
<title>A Still Brook – Business Card</title>
<link rel="stylesheet" href="https://fonts.googleapis.com/css2?family=Great+Vibes&family=Open+Sans:wght@400;600&family=Arimo:wght@400&display=swap">
<style>
  :root {
    --page-bg: #e9ebee;
    --card-white: #ffffff;
    --sky-blue: #3fa6df;
    --accent-green: #2f8a3c;
    --accent-navy: #2a2e8e;
    --title-blue: #1b4e72;
    --role-teal: #2b6a90;
    --ink: #1d1d1d;
    --service-red: #86301c;
    --badge-ring: #6b6b6b;
    --listing-tint: #dbe4ef;
    --water-light: #dfeef7;
    --water-mid: #8fc3e3;
    --stone-blue: #2b6fa6;
  }
  * { box-sizing: border-box; margin: 0; padding: 0; }
  html, body {
    width: 1200px; height: 1200px; overflow: hidden;
    background: var(--page-bg);
  }
  .sheet {
    position: relative; width: 1200px; height: 1200px;
  }
  .card {
    --accent: var(--accent-green);
    position: absolute; left: 150px;
    width: 900px; height: 555px;
    background: var(--card-white);
    overflow: hidden;
    box-shadow: 0 6px 18px rgba(0,0,0,0.18);
  }
  .card--green { top: 30px; }
  .card--navy { top: 615px; --accent: var(--accent-navy); }
  .card__shapes { position: absolute; inset: 0; width: 900px; height: 555px; }
  .card__shapes .sky { fill: var(--sky-blue); }
  .card__shapes .corner { fill: var(--card-white); }
  .card__shapes .stripe { fill: none; stroke: var(--accent); stroke-width: 9; }
  .card__shapes .listing { fill: var(--listing-tint); }
  .card__shapes .badge { fill: var(--card-white); stroke: var(--badge-ring); stroke-width: 3; }

  .water {
    position: absolute; left: 240px; right: 0; bottom: 0; height: 80px;
    background:
      linear-gradient(180deg, rgba(255,255,255,0) 0%, var(--water-light) 100%),
      linear-gradient(180deg, var(--card-white) 0%, var(--stone-blue) 35%, var(--water-mid) 65%, var(--water-light) 100%);
  }

  .details {
    position: absolute; left: 420px; width: 480px; top: 0;
    text-align: center;
  }
  .brand {
    position: absolute; left: 480px; top: 62px; width: 420px;
    text-align: center;
    font-family: "Great Vibes", cursive;
    font-size: 64px; line-height: 1; color: var(--title-blue);
  }
  .name {
    position: absolute; left: 0; right: 0; top: 166px;
    font-family: "Open Sans", sans-serif; font-weight: 600;
    font-size: 25px; color: var(--ink);
  }
  .role {
    position: absolute; left: 0; right: 0; top: 199px;
    font-family: "Arimo", sans-serif; font-size: 21px; line-height: 29px;
    color: var(--role-teal);
  }
  .contact {
    position: absolute; left: 0; right: 0; top: 303px;
    font-family: "Arimo", sans-serif; font-size: 20px; line-height: 28px;
    color: var(--ink);
  }
  .contact .email { font-size: 18.5px; }
  .services-lead {
    position: absolute; left: 0; right: 0; top: 375px;
    font-family: "Open Sans", sans-serif; font-size: 18px;
    color: var(--service-red);
  }
  .services {
    position: absolute; left: 140px; top: 403px; width: 320px;
    list-style: none;
    display: grid; grid-template-columns: 165px 155px; grid-auto-flow: column; grid-template-rows: repeat(3, 27px);
    font-family: "Open Sans", sans-serif; font-size: 17px; color: var(--ink);
    text-align: left;
  }
  .services li { display: flex; align-items: center; gap: 7px; }
  .services svg { width: 13px; height: 13px; flex: none; }
  .services svg path { fill: none; stroke: var(--ink); stroke-width: 2.4; stroke-linecap: round; stroke-linejoin: round; }
</style>
</head>
<body>
<main class="sheet">

  <section class="card card--green" aria-label="Business card, green accent">
    <svg class="card__shapes" viewBox="0 0 746 460" preserveAspectRatio="none" aria-hidden="true">
      <path class="sky" d="M0,0 H290 C240,110 180,230 170,460 H0 Z"/>
      <circle class="corner" cx="60" cy="-30" r="165"/>
      <path class="stripe" d="M293,-5 C243,110 183,230 174,465"/>
      <rect class="listing" x="18" y="32" width="110" height="50" rx="3"/>
      <circle class="badge" cx="195" cy="225" r="85"/>
    </svg>
    <div class="water" role="img" aria-label="Photo of smooth blue stones resting on calm water"></div>
    <div class="brand">A Still Brook</div>
    <div class="details">
      <p class="name">Janet Callory</p>
      <p class="role">Clinical Hypnotherapist and Counsellor<br>BA Social Work Dip Clinical Hypnotherapy<br>and Psychotherapy</p>
      <p class="contact">Phone: 0438157302<br><span class="email">Email: astillbrookhypnotherapy@fernmail.example</span></p>
      <p class="services-lead">Provide hypnotherapy and counselling for</p>
      <ul class="services">
        <li><svg viewBox="0 0 14 14"><path d="M2,7.5 L5.5,11 L12,3"/></svg>Addictions</li>
        <li><svg viewBox="0 0 14 14"><path d="M2,7.5 L5.5,11 L12,3"/></svg>Weight loss</li>
        <li><svg viewBox="0 0 14 14"><path d="M2,7.5 L5.5,11 L12,3"/></svg>Anxiety</li>
        <li><svg viewBox="0 0 14 14"><path d="M2,7.5 L5.5,11 L12,3"/></svg>Depression</li>
        <li><svg viewBox="0 0 14 14"><path d="M2,7.5 L5.5,11 L12,3"/></svg>Smoking</li>
        <li><svg viewBox="0 0 14 14"><path d="M2,7.5 L5.5,11 L12,3"/></svg>Alcohol</li>
      </ul>
    </div>
  </section>

  <section class="card card--navy" aria-label="Business card, navy accent">
    <svg class="card__shapes" viewBox="0 0 746 460" preserveAspectRatio="none" aria-hidden="true">
      <path class="sky" d="M0,0 H290 C240,110 180,230 170,460 H0 Z"/>
      <circle class="corner" cx="60" cy="-30" r="165"/>
      <path class="stripe" d="M293,-5 C243,110 183,230 174,465"/>
      <rect class="listing" x="18" y="32" width="110" height="50" rx="3"/>
      <circle class="badge" cx="195" cy="225" r="85"/>
    </svg>
    <div class="water" role="img" aria-label="Photo of smooth blue stones resting on calm water"></div>
    <div class="brand">A Still Brook</div>
    <div class="details">
      <p class="name">Janet Callory</p>
      <p class="role">Clinical Hypnotherapist and Counsellor<br>BA Social Work Dip Clinical Hypnotherapy<br>and Psychotherapy</p>
      <p class="contact">Phone: 0438157302<br><span class="email">Email: astillbrookhypnotherapy@fernmail.example</span></p>
      <p class="services-lead">Provide hypnotherapy and counselling for</p>
      <ul class="services">
        <li><svg viewBox="0 0 14 14"><path d="M2,7.5 L5.5,11 L12,3"/></svg>Addictions</li>
        <li><svg viewBox="0 0 14 14"><path d="M2,7.5 L5.5,11 L12,3"/></svg>Weight loss</li>
        <li><svg viewBox="0 0 14 14"><path d="M2,7.5 L5.5,11 L12,3"/></svg>Anxiety</li>
        <li><svg viewBox="0 0 14 14"><path d="M2,7.5 L5.5,11 L12,3"/></svg>Depression</li>
        <li><svg viewBox="0 0 14 14"><path d="M2,7.5 L5.5,11 L12,3"/></svg>Smoking</li>
        <li><svg viewBox="0 0 14 14"><path d="M2,7.5 L5.5,11 L12,3"/></svg>Alcohol</li>
      </ul>
    </div>
  </section>

</main>
</body>
</html>
```